Roofing Company Sales Rep Business Card

Business card for sales rep to canvass and hand out to property owners/managers for free roof inspections and roof replacements.

```html
<!DOCTYPE html>
<html lang="en">
<head>
<meta charset="utf-8">
<title>Keystone Roofing – Business Card</title>
<link href="https://fonts.googleapis.com/css2?family=Montserrat:wght@400;500;800&display=swap" rel="stylesheet">
<style>
  :root {
    --bg: #e9e9eb;
    --card-dark: #151516;
    --card-light: #ffffff;
    --brand-red: #e21f26;
    --ink: #111111;
    --grey-mark: #d6d6da;
  }
  * { margin: 0; padding: 0; box-sizing: border-box; }
  html, body { width: 1200px; height: 1200px; overflow: hidden; }
  body {
    background: var(--bg);
    font-family: "Montserrat", sans-serif;
    display: flex;
    flex-direction: column;
    align-items: center;
    justify-content: center;
    gap: 60px;
  }
  .card {
    position: relative;
    width: 900px;
    height: 514px;
    border-radius: 28px;
    overflow: hidden;
    box-shadow: 0 6px 18px rgba(0,0,0,.18);
  }

  /* Back side */
  .card-back {
    background: var(--card-dark);
    display: flex;
    align-items: center;
    justify-content: center;
  }
  .brand-lockup {
    display: flex;
    align-items: center;
    gap: 18px;
  }
  .brand-square {
    width: 34px;
    height: 34px;
    background: var(--brand-red);
    flex: none;
  }
  .brand-name {
    font-weight: 800;
    letter-spacing: 3px;
    text-transform: uppercase;
    line-height: 1;
    white-space: nowrap;
  }
  .card-back .brand-name {
    color: var(--grey-mark);
    font-size: 50px;
  }

  /* Front side */
  .card-front { background: var(--card-light); }
  .front-wave {
    position: absolute;
    inset: 0;
    width: 100%;
    height: 100%;
  }
  .front-brand {
    position: absolute;
    left: 50px;
    top: 222px;
    gap: 12px;
  }
  .card-front .brand-name {
    color: var(--ink);
    font-size: 25px;
    letter-spacing: 1px;
  }
  .card-front .brand-square { width: 22px; height: 22px; }
  .front-divider {
    position: absolute;
    left: 440px;
    top: 132px;
    width: 2px;
    height: 170px;
    background: var(--brand-red);
  }
  .contact-block {
    position: absolute;
    left: 466px;
    top: 108px;
    color: var(--ink);
  }
  .person-name {
    font-weight: 800;
    font-size: 30px;
    letter-spacing: .5px;
    text-transform: uppercase;
    line-height: 1.05;
    white-space: nowrap;
  }
  .person-name .surname { color: var(--brand-red); }
  .person-role {
    font-size: 18px;
    font-weight: 500;
    margin: 4px 0 8px 20px;
  }
  .contact-list { list-style: none; }
  .contact-list li {
    display: flex;
    align-items: center;
    gap: 10px;
    font-size: 18px;
    font-weight: 500;
    line-height: 1.55;
    margin-left: 20px;
    white-space: nowrap;
  }
  .contact-list svg { width: 18px; height: 18px; flex: none; fill: var(--brand-red); }
</style>
</head>
<body>

  <section class="card card-back" aria-label="Card back">
    <div class="brand-lockup">
      <span class="brand-square"></span>
      <span class="brand-name">Keystone Roofing</span>
    </div>
  </section>

  <section class="card card-front" aria-label="Card front">
    <svg class="front-wave" viewBox="0 0 900 514" preserveAspectRatio="none" aria-hidden="true">
      <path d="M0,486 C380,486 620,400 900,312 L900,514 L0,514 Z" fill="var(--brand-red)"/>
      <path d="M0,468 C380,468 620,382 900,292" fill="none" stroke="var(--ink)" stroke-width="6"/>
    </svg>

    <div class="brand-lockup front-brand">
      <span class="brand-square"></span>
      <span class="brand-name">Keystone Roofing</span>
    </div>

    <div class="front-divider"></div>

    <div class="contact-block">
      <h1 class="person-name">Dale <span class="surname">Morrow</span></h1>
      <p class="person-role">Co-Founder</p>
      <ul class="contact-list">
        <li>
          <svg viewBox="0 0 24 24"><path d="M6.6 10.8a15.1 15.1 0 0 0 6.6 6.6l2.2-2.2c.3-.3.7-.4 1-.2 1.1.4 2.3.6 3.6.6.6 0 1 .4 1 1V20c0 .6-.4 1-1 1A17 17 0 0 1 3 4c0-.6.4-1 1-1h3.5c.6 0 1 .4 1 1 0 1.3.2 2.5.6 3.6.1.3 0 .7-.2 1z"/></svg>
          555.014.2276
        </li>
        <li>
          <svg viewBox="0 0 24 24"><path d="M2 5h20v14H2z" opacity=".25"/><path d="M2 5h20v2l-10 6L2 7zM2 9l10 6 10-6v10H2z"/></svg>
          hello@keystoneroof.com
        </li>
        <li>
          <svg viewBox="0 0 24 24"><path d="M12 2a10 10 0 1 0 0 20 10 10 0 0 0 0-20zm6.9 6h-3a15 15 0 0 0-1.3-3.9A8 8 0 0 1 18.9 8zM12 4c.8 1.2 1.5 2.5 1.9 4h-3.8c.4-1.5 1.1-2.8 1.9-4zM4.3 14a8 8 0 0 1 0-4h3.4a16 16 0 0 0 0 4zm.8 2h3a15 15 0 0 0 1.3 3.9A8 8 0 0 1 5.1 16zm3-8h-3a8 8 0 0 1 4.3-3.9C8.8 5.3 8.4 6.600 8.1 8zM12 20c-.8-1.2-1.5-2.5-1.900-4h3.8c-.4 1.5-1.1 2.8-1.9 4zm2.3-6H9.7a14 14 0 0 1 0-4h4.6a14 14 0 0 1 0 4zm.3 5.9c.6-1.2 1-2.5 1.3-3.9h3a8 8 0 0 1-4.3 3.9zm1.7-5.9a16 16 0 0 0 0-4h3.4a8 8 0 0 1 0 4z"/></svg>
          www.keystoneroof.com
        </li>
        <li>
          <svg viewBox="0 0 24 24"><path d="M12 2a7 7 0 0 0-7 7c0 5.2 7 13 7 13s7-7.8 7-13a7 7 0 0 0-7-7zm0 9.5A2.5 2.5 0 1 1 12 6.5a2.5 2.5 0 0 1 0 5z"/></svg>
          14 Cedar Lane 8, Riverton
        </li>
      </ul>
    </div>
  </section>

</body>
</html>
```